Vodka Carton Design

We need a design completed for our 6x700ml vodka carton.
We currently have a bottle label designed and would like an outer packaging design created for the 6 x 700ml vodka carton.

We would like the packaging design to be similar to our current bottle label design for consistency in our product branding but artistic freedom and variation is encouraged. (images of bottle have been attached)

Certain particulars and compulsory elements for the design have been outlined below.

The dimensions of the carton are
H = 320mm
L=224mm
W = 150mm

- Due to industry requirements, the label must have the following design elements included

- a pregnancy warning label with the correct sizing on the design (requirements attached and high def image of decal attached)

- barcode (attached)

The name of the vodka product is called
"Ninefold Vodka - Lantern Series" and our company name is called
"Ninefold Distilling Co" (logos attached)

Good luck !

Need extra days to review

```html
<!DOCTYPE html>
<html lang="en">
<head>
<meta charset="utf-8">
<title>Ninefold Vodka – Lantern Series 6x700ml Carton</title>
<link rel="stylesheet" href="https://fonts.googleapis.com/css2?family=Karla:wght@400;600;700&family=Libre+Baskerville:wght@700&family=Pinyon+Script&display=swap">
<style>
  :root {
    --ink: #322c2b;
    --royal: #2e3192;
    --warn-red: #e31e24;
    --paper: #ffffff;
    --flap: #fdfcfd;
    --rule: #9a9a9a;
    --code-area: #f4f4f4;
    --serif: "Libre Baskerville", Georgia, serif;
    --sans: "Karla", Arial, sans-serif;
    --script: "Pinyon Script", cursive;
  }
  * { box-sizing: border-box; margin: 0; padding: 0; }
  html, body { width: 1200px; height: 735px; overflow: hidden; background: var(--paper); }
  .carton { position: relative; width: 1200px; height: 735px; background: var(--paper); color: var(--ink); font-family: var(--sans); }

  /* dieline */
  .flap { position: absolute; background: var(--flap); border: 1px solid var(--rule); }
  .flap--top { top: 0; height: 118px; }
  .flap--bottom { top: 617px; height: 118px; }
  .glue-flap { position: absolute; left: 0; top: 117px; width: 32px; height: 501px; border: 1px solid var(--rule); border-right: none; }
  .band { position: absolute; left: 31px; width: 1169px; height: 18px; background: var(--ink); }
  .band--top { top: 117px; }
  .band--bottom { top: 599px; }

  /* side panel */
  .side-panel { position: absolute; top: 0; width: 235px; height: 735px; text-align: center; }
  .side-panel > * { position: absolute; left: 0; width: 100%; }
  .side-kicker { top: 147px; font: 700 17px/1 var(--serif); letter-spacing: 5px; padding-left: 5px; }
  .side-title { top: 170px; font: 700 34px/1 var(--serif); letter-spacing: 6px; padding-left: 6px; }
  .side-series { top: 211px; left: 29px !important; width: 177px !important; height: 32px; background: var(--ink); color: var(--paper); font: 600 13.5px/32px var(--sans); letter-spacing: 2.5px; }
  .side-copy { top: 262px; font: 600 10.8px/16px var(--sans); letter-spacing: 0.2px; }
  .side-script { top: 318px; font: 400 18px/1 var(--script); }
  .side-maker { top: 340px; font: 700 12.6px/1 var(--sans); letter-spacing: 1.2px; }
  .side-web { top: 372px; font: 700 11px/1 var(--sans); letter-spacing: 0.3px; }
  .side-address { top: 387px; font: 600 8.8px/1 var(--sans); letter-spacing: 0.3px; }

  .warning { top: 413px; left: 40px !important; width: 155px !important; height: 36px; border: 1px solid var(--ink); display: flex; align-items: center; gap: 4px; padding: 0 3px; text-align: left; }
  .warning__pictogram { width: 27px; height: 27px; border-radius: 50%; border: 2px solid var(--warn-red); background: #f3c9ca; flex: none; }
  .warning__title { color: var(--warn-red); font: 700 10.4px/1 var(--sans); }
  .warning__text { font: 400 9.4px/9.4px var(--sans); }

  .handling { top: 464px; left: 42px !important; width: 152px !important; display: flex; gap: 6px; }
  .handling svg { width: 33px; height: 33px; }

  .std-drinks { top: 504px; left: 14px !important; width: 50px !important; }
  .std-drinks__count { font: 400 14px/1 var(--sans); }
  .std-drinks__badge { position: relative; width: 48px; height: 54px; margin-top: 2px; }
  .std-drinks__badge svg { position: absolute; inset: 0; }
  .std-drinks__label { position: absolute; top: 3px; left: 0; width: 100%; font: 400 7px/7px var(--sans); }
  .std-drinks__num { position: absolute; top: 18px; left: 0; width: 100%; font: 400 22px/1 var(--sans); }
  .std-drinks__approx { position: absolute; top: 43px; left: 0; width: 100%; font: 400 5.2px/1 var(--sans); }

  .barcode-area { top: 511px; left: 75px !important; width: 90px !important; height: 73px; background: var(--code-area); border: 1px solid var(--ink); }

  .weight { top: 524px; left: 176px !important; width: 50px !important; height: 48px; }
  .weight svg { position: absolute; inset: 0; }
  .weight__value { position: absolute; top: 24px; left: 0; width: 100%; color: var(--paper); font: 700 11px/1 var(--sans); }

  /* front panel */
  .front-panel { position: absolute; top: 0; width: 350px; height: 735px; text-align: center; }
  .front-panel > * { position: absolute; }
  .ribbon { left: 0; top: 0; width: 350px; height: 735px; }
  .ribbon-mark { left: 127px; width: 95px; color: var(--paper); }
  .ribbon-mark__dot { display: block; width: 44px; height: 44px; margin: 0 auto 10px; border: 1.5px solid var(--paper); border-radius: 50%; }
  .ribbon-mark__name { font: 400 9.5px/10px var(--sans); letter-spacing: 0.2px; }
  .ribbon-mark--one { top: 24px; }
  .ribbon-mark--two { top: 134px; }

  .brand-mark { top: 288px; left: 0; width: 100%; display: flex; align-items: center; justify-content: center; gap: 8px; font: 700 28px/1 var(--serif); letter-spacing: 3px; }
  .brand-mark__square { width: 18px; height: 18px; background: var(--ink); }

  .front-kicker { top: 361px; left: 0; width: 100%; font: 700 22px/1 var(--serif); letter-spacing: 7px; padding-left: 7px; }
  .front-title { top: 388px; left: 0; width: 100%; font: 700 48px/1 var(--serif); letter-spacing: 8px; padding-left: 8px; }
  .front-series { top: 517px; left: 34px; width: 282px; height: 32px; background: var(--ink); color: var(--paper); font: 600 16.5px/32px var(--sans); letter-spacing: 3px; }
  .abv { top: 553px; left: 30px; width: 86px; font: 400 16px/18px var(--sans); }
  .abv strong { font-weight: 600; }
  .pack { top: 550px; left: 127px; width: 95px; color: var(--paper); }
  .pack__count { font: 600 41px/38px var(--sans); }
  .pack__volume { font: 600 13.5px/1 var(--sans); margin-top: 3px; }
  .batch { top: 554px; left: 240px; width: 80px; font: 400 16.5px/1 var(--sans); }
</style>
</head>
<body>
<main class="carton">
  <div class="flap flap--top" style="left:31px;width:236px"></div>
  <div class="flap flap--top" style="left:266px;width:351px"></div>
  <div class="flap flap--top" style="left:616px;width:235px"></div>
  <div class="flap flap--top" style="left:850px;width:350px"></div>
  <div class="flap flap--bottom" style="left:31px;width:236px"></div>
  <div class="flap flap--bottom" style="left:266px;width:351px"></div>
  <div class="flap flap--bottom" style="left:616px;width:235px"></div>
  <div class="flap flap--bottom" style="left:850px;width:350px"></div>
  <div class="glue-flap"></div>
  <div class="band band--top"></div>
  <div class="band band--bottom"></div>

  <!-- side panel A -->
  <section class="side-panel" style="left:31px">
    <p class="side-kicker">NINEFOLD</p>
    <h2 class="side-title">VODKA</h2>
    <p class="side-series">LANTERN SERIES</p>
    <p class="side-copy">This smooth, clean tasting Vodka<br>is perfect on its own, over ice,<br>or any cocktail.</p>
    <p class="side-script">Distilled and bottled by</p>
    <p class="side-maker">NINEFOLD DISTILLING CO.</p>
    <p class="side-web">www.ninefolddistilling.com.au</p>
    <p class="side-address">14/8 larkspur lane, Eastvale 6120 wa</p>
    <div class="warning">
      <span class="warning__pictogram" role="img" aria-label="Pregnancy warning pictogram"></span>
      <div><p class="warning__title">PREGNANCY WARNING</p><p class="warning__text">Alcohol can cause lifelong<br>harm to your baby</p></div>
    </div>
    <div class="handling">
      <svg viewBox="0 0 33 33" aria-label="This way up"><rect x="1" y="1" width="31" height="31" rx="4" fill="none" stroke="#322c2b" stroke-width="1.6"/><path d="M11 25V10M7 14l4-6 4 6M22 25V10M18 14l4-6 4 6M7 27h19" fill="none" stroke="#322c2b" stroke-width="2.2"/></svg>
      <svg viewBox="0 0 33 33" aria-label="Keep dry"><rect x="1" y="1" width="31" height="31" rx="4" fill="none" stroke="#322c2b" stroke-width="1.6"/><path d="M6 17a10.5 9 0 0 1 21 0z" fill="#322c2b"/><path d="M16.5 17v8a2 2 0 0 1-4 0" fill="none" stroke="#322c2b" stroke-width="1.6"/></svg>
      <svg viewBox="0 0 33 33" aria-label="Fragile"><rect x="1" y="1" width="31" height="31" rx="4" fill="none" stroke="#322c2b" stroke-width="1.6"/><path d="M10 6h13l-1 8a5.5 5.5 0 0 1-11 0z" fill="#322c2b"/><path d="M16.5 19v7M12 27h9" stroke="#322c2b" stroke-width="2"/></svg>
      <svg viewBox="0 0 33 33" aria-label="Recyclable"><rect x="1" y="1" width="31" height="31" rx="4" fill="none" stroke="#322c2b" stroke-width="1.6"/><path d="M13 9l3.5-3 3.5 6M24 18l2 5-6 1M9 24l-3-5 4-5" fill="none" stroke="#322c2b" stroke-width="2.4"/><path d="M19 8l-3 4h6zM21 26l3-4-5-1zM8 16l5-1-2 5z" fill="#322c2b"/></svg>
    </div>
    <div class="std-drinks">
      <p class="std-drinks__count">6x</p>
      <div class="std-drinks__badge">
        <svg viewBox="0 0 48 54"><path d="M1 1h46v12l-5 2-4 38H10L6 15 1 13z" fill="none" stroke="#322c2b" stroke-width="1.3"/></svg>
        <p class="std-drinks__label">STANDARD<br>DRINKS</p>
        <p class="std-drinks__num">21</p>
        <p class="std-drinks__approx">APPROX.</p>
      </div>
    </div>
    <div class="barcode-area" role="img" aria-label="Reserved area for the product barcode"></div>
    <div class="weight">
      <svg viewBox="0 0 50 48"><rect x="19" y="1" width="12" height="11" fill="none" stroke="#000" stroke-width="2"/><path d="M9 12h32l9 36H0z" fill="#000"/></svg>
      <p class="weight__value">7.5 kg</p>
    </div>
  </section>

  <!-- front panel A -->
  <section class="front-panel" style="left:266px">
    <svg class="ribbon" viewBox="0 0 350 735" aria-hidden="true">
      <path d="M127 0h95v252l-47.5-34L127 252z" fill="#2e3192"/>
      <path d="M131 0v241l43.5-31 43.5 31V0" fill="none" stroke="#fff" stroke-width="1.3"/>
      <path d="M127 453l47.5 34 47.5-34v164h-95z" fill="#2e3192"/>
      <path d="M131 460l43.5 31 43.5-31v157M131 460v157" fill="none" stroke="#fff" stroke-width="1.3"/>
    </svg>
    <div class="ribbon-mark ribbon-mark--one"><span class="ribbon-mark__dot"></span><p class="ribbon-mark__name">NINEFOLD<br>DISTILLING CO.</p></div>
    <div class="ribbon-mark ribbon-mark--two"><span class="ribbon-mark__dot"></span><p class="ribbon-mark__name">NINEFOLD<br>DISTILLING CO.</p></div>
    <p class="brand-mark"><span class="brand-mark__square"></span>NINEFOLD</p>
    <p class="front-kicker">NINEFOLD</p>
    <h1 class="front-title">VODKA</h1>
    <p class="front-series">LANTERN SERIES</p>
    <p class="abv"><strong>37.5 %</strong><br>ALC/VOL</p>
    <div class="pack"><p class="pack__count">6x</p><p class="pack__volume">700 ml</p></div>
    <p class="batch">BATCH#</p>
  </section>

  <!-- side panel B -->
  <section class="side-panel" style="left:616px">
    <p class="side-kicker">NINEFOLD</p>
    <h2 class="side-title">VODKA</h2>
    <p class="side-series">LANTERN SERIES</p>
    <p class="side-copy">This smooth, clean tasting Vodka<br>is perfect on its own, over ice,<br>or any cocktail.</p>
    <p class="side-script">Distilled and bottled by</p>
    <p class="side-maker">NINEFOLD DISTILLING CO.</p>
    <p class="side-web">www.ninefolddistilling.com.au</p>
    <p class="side-address">14/8 larkspur lane, Eastvale 6120 wa</p>
    <div class="warning">
      <span class="warning__pictogram" role="img" aria-label="Pregnancy warning pictogram"></span>
      <div><p class="warning__title">PREGNANCY WARNING</p><p class="warning__text">Alcohol can cause lifelong<br>harm to your baby</p></div>
    </div>
    <div class="handling">
      <svg viewBox="0 0 33 33" aria-label="This way up"><rect x="1" y="1" width="31" height="31" rx="4" fill="none" stroke="#322c2b" stroke-width="1.6"/><path d="M11 25V10M7 14l4-6 4 6M22 25V10M18 14l4-6 4 6M7 27h19" fill="none" stroke="#322c2b" stroke-width="2.2"/></svg>
      <svg viewBox="0 0 33 33" aria-label="Keep dry"><rect x="1" y="1" width="31" height="31" rx="4" fill="none" stroke="#322c2b" stroke-width="1.6"/><path d="M6 17a10.5 9 0 0 1 21 0z" fill="#322c2b"/><path d="M16.5 17v8a2 2 0 0 1-4 0" fill="none" stroke="#322c2b" stroke-width="1.6"/></svg>
      <svg viewBox="0 0 33 33" aria-label="Fragile"><rect x="1" y="1" width="31" height="31" rx="4" fill="none" stroke="#322c2b" stroke-width="1.6"/><path d="M10 6h13l-1 8a5.5 5.5 0 0 1-11 0z" fill="#322c2b"/><path d="M16.5 19v7M12 27h9" stroke="#322c2b" stroke-width="2"/></svg>
      <svg viewBox="0 0 33 33" aria-label="Recyclable"><rect x="1" y="1" width="31" height="31" rx="4" fill="none" stroke="#322c2b" stroke-width="1.6"/><path d="M13 9l3.5-3 3.5 6M24 18l2 5-6 1M9 24l-3-5 4-5" fill="none" stroke="#322c2b" stroke-width="2.4"/><path d="M19 8l-3 4h6zM21 26l3-4-5-1zM8 16l5-1-2 5z" fill="#322c2b"/></svg>
    </div>
    <div class="std-drinks">
      <p class="std-drinks__count">6x</p>
      <div class="std-drinks__badge">
        <svg viewBox="0 0 48 54"><path d="M1 1h46v12l-5 2-4 38H10L6 15 1 13z" fill="none" stroke="#322c2b" stroke-width="1.3"/></svg>
        <p class="std-drinks__label">STANDARD<br>DRINKS</p>
        <p class="std-drinks__num">21</p>
        <p class="std-drinks__approx">APPROX.</p>
      </div>
    </div>
    <div class="barcode-area" role="img" aria-label="Reserved area for the product barcode"></div>
    <div class="weight">
      <svg viewBox="0 0 50 48"><rect x="19" y="1" width="12" height="11" fill="none" stroke="#000" stroke-width="2"/><path d="M9 12h32l9 36H0z" fill="#000"/></svg>
      <p class="weight__value">7.5 kg</p>
    </div>
  </section>

  <!-- front panel B -->
  <section class="front-panel" style="left:850px">
    <svg class="ribbon" viewBox="0 0 350 735" aria-hidden="true">
      <path d="M127 0h95v252l-47.5-34L127 252z" fill="#2e3192"/>
      <path d="M131 0v241l43.5-31 43.5 31V0" fill="none" stroke="#fff" stroke-width="1.3"/>
      <path d="M127 453l47.5 34 47.5-34v164h-95z" fill="#2e3192"/>
      <path d="M131 460l43.5 31 43.5-31v157M131 460v157" fill="none" stroke="#fff" stroke-width="1.3"/>
    </svg>
    <div class="ribbon-mark ribbon-mark--one"><span class="ribbon-mark__dot"></span><p class="ribbon-mark__name">NINEFOLD<br>DISTILLING CO.</p></div>
    <div class="ribbon-mark ribbon-mark--two"><span class="ribbon-mark__dot"></span><p class="ribbon-mark__name">NINEFOLD<br>DISTILLING CO.</p></div>
    <p class="brand-mark"><span class="brand-mark__square"></span>NINEFOLD</p>
    <p class="front-kicker">NINEFOLD</p>
    <h2 class="front-title">VODKA</h2>
    <p class="front-series">LANTERN SERIES</p>
    <p class="abv"><strong>37.5 %</strong><br>ALC/VOL</p>
    <div class="pack"><p class="pack__count">6x</p><p class="pack__volume">700 ml</p></div>
    <p class="batch">BATCH#</p>
  </section>
</main>
</body>
</html>
```